Need Bus charter business website,

I am starting a bus charter business in the near future. I am based in Geelong, Victoria in Australia. I will have a 25 or 28 seater bus that will be used to take people on charted trips. Whether they be to birthday parties, weddings, sporting events, corporate events, mystery trips, going down the Great Ocean Road, or anywhere someone wants. As for colour scheme, I'm leaning towards something blue and grey, but open to anything really that catches my eye. I played around with a basic web design program and made a basic site which I uploaded ( www.kelvomtravel.com.au) It has things which I wanted to include such as, services I will provide, trip information, contact form etc.

I don't mind if the layout is completely different to my site as it was only a template that was included in the program I used. I would like the overall design to be relatively fluid, not having to back-track a lot to navigate the site.

```html
<!DOCTYPE html>
<html lang="en">
<head>
<meta charset="utf-8">
<title>Kelvom Travel</title>
<link href="https://fonts.googleapis.com/css2?family=Arimo:wght@400;700&family=Bebas+Neue&display=swap" rel="stylesheet">
<style>
  :root {
    --page-bg: #efefe9;
    --white: #ffffff;
    --band: #d9d9d7;
    --line: #dcdcdc;
    --text: #7a7a7a;
    --text-dark: #555555;
    --heading-soft: #c4c4c4;
    --accent: #9d9dc8;
    --icon: #b9b9b9;
    --icon-dark: #6f6f6f;
  }
  * { box-sizing: border-box; margin: 0; padding: 0; }
  html, body { width: 1200px; height: 856px; overflow: hidden; }
  body {
    position: relative;
    background: var(--page-bg);
    font-family: "Arimo", Arial, sans-serif;
    color: var(--text);
  }

  /* top bar */
  .topbar {
    position: absolute; left: 0; top: 0; width: 1200px; height: 46px;
    background: var(--white); border-bottom: 1px solid var(--line);
  }
  .topbar__contact {
    position: absolute; left: 119px; top: 15px; font-size: 14px; color: var(--text);
  }
  .topbar__contact strong { color: var(--text-dark); }
  .main-nav {
    position: absolute; left: 563px; top: 0; height: 46px; display: flex;
    border-left: 1px solid var(--line);
  }
  .main-nav a {
    display: block; height: 46px; line-height: 46px; padding: 0 12px;
    font-size: 14px; color: var(--text); text-decoration: none;
    border-right: 1px solid var(--line);
  }

  /* header band */
  .header-band {
    position: absolute; left: 0; top: 46px; width: 1200px; height: 102px;
    background: var(--band); border-bottom: 2px solid #cfcfcd;
    height: 102px;
  }
  .header-band { height: 103px; }
  .brand {
    position: absolute; left: 120px; top: 11px; width: 119px; height: 52px;
    background: var(--white); display: flex; align-items: center; justify-content: center;
    font-family: "Arimo", Arial, sans-serif; font-weight: 700; font-size: 15px; color: #111;
  }
  .social {
    position: absolute; display: flex; background: var(--white);
  }
  .social__item {
    width: 47px; height: 48px; border-left: 1px solid var(--line);
    display: flex; align-items: center; justify-content: center;
  }
  .social--header { right: 58px; top: 10px; }

  /* slider */
  .slider {
    position: absolute; left: 119px; top: 155px; width: 1023px; height: 358px;
    background: var(--white); border: 1px solid var(--line); padding: 6px;
  }
  .slider__photo {
    width: 100%; height: 100%;
    background: linear-gradient(120deg, #d9c3bb 0%, #e8cfc3 30%, #b8232a 55%, #7d0f16 80%, #c9cdd6 100%);
  }
  .slider__controls {
    position: absolute; left: 1044px; top: 515px; display: flex; background: var(--white);
    border: 1px solid var(--line);
  }
  .slider__controls span {
    width: 48px; height: 46px; display: flex; align-items: center; justify-content: center;
  }
  .slider__controls span + span { border-left: 1px solid var(--line); }

  /* welcome */
  .welcome {
    position: absolute; left: 119px; top: 566px; width: 1023px; height: 54px;
    background: var(--white); border: 1px solid var(--line);
    font-family: "Bebas Neue", Impact, sans-serif; font-size: 28px; color: var(--heading-soft);
    text-align: center; line-height: 54px; letter-spacing: 0.3px;
  }
  .welcome__notch { position: absolute; left: 500px; bottom: -12px; }

  /* service cards */
  .service {
    position: absolute; top: 665px; width: 320px; height: 200px;
    background: var(--white); border: 1px solid var(--line);
  }
  .service--parties { left: 119px; }
  .service--charters { left: 470px; }
  .service--corporate { left: 820px; }
  .service__icon { position: absolute; left: 26px; top: 26px; }
  .service__title {
    position: absolute; left: 104px; top: 22px;
    font-family: "Bebas Neue", Impact, sans-serif; font-weight: 400; font-size: 28px; color: var(--accent);
  }
  .service__text {
    position: absolute; left: 8px; right: 8px; top: 90px;
    font-size: 16px; line-height: 20px; text-align: center; color: var(--text);
  }

  /* footer */
  .site-footer {
    position: absolute; left: 0; top: 805px; width: 1200px; height: 51px;
    background: var(--white); border-top: 1px solid var(--line);
  }
  .site-footer__copy { position: absolute; left: 119px; top: 17px; font-size: 14px; color: var(--text); }
  .social--footer { right: 58px; top: 2px; }
</style>
</head>
<body>

<header class="topbar">
  <p class="topbar__contact"><strong>Email:</strong> info@kelvomtravel.com.au | <strong>Phone:</strong> (+61) XXXX XXX XXX</p>
  <nav class="main-nav">
    <a href="#">Kelvom Travel</a>
    <a href="#">About Us</a>
    <a href="#">Services</a>
    <a href="#">Trips on Offers</a>
    <a href="#">Book a Trip</a>
    <a href="#">Contact Us</a>
  </nav>
</header>

<div class="header-band">
  <div class="brand">Kelvom Travel</div>
  <div class="social social--header">
    <span class="social__item"><svg width="28" height="28" viewBox="0 0 28 28"><circle cx="14" cy="14" r="12" fill="none" stroke="#c9c9c9" stroke-width="2.5"/><path d="M14 7v14M7 14h14" stroke="#c9c9c9" stroke-width="3"/></svg></span>
    <span class="social__item"><svg width="22" height="22"><circle cx="11" cy="11" r="9" fill="#c9c9c9"/></svg></span>
    <span class="social__item"><svg width="22" height="22"><circle cx="11" cy="11" r="9" fill="#c9c9c9"/></svg></span>
    <span class="social__item"><svg width="22" height="22"><circle cx="11" cy="11" r="9" fill="#c9c9c9"/></svg></span>
    <span class="social__item"><svg width="22" height="22"><circle cx="11" cy="11" r="9" fill="#c9c9c9"/></svg></span>
    <span class="social__item" style="border-right:1px solid var(--line)"><svg width="22" height="22"><circle cx="11" cy="11" r="9" fill="#c9c9c9"/></svg></span>
  </div>
</div>

<section class="slider">
  <div class="slider__photo" role="img" aria-label="Close-up of a couple's hands with wedding rings resting on a bouquet of red roses"></div>
</section>
<div class="slider__controls">
  <span><svg width="12" height="24"><path d="M11 1L1 12l10 11z" fill="#c9c9c9"/></svg></span>
  <span><svg width="12" height="24"><path d="M1 1l10 11L1 23z" fill="#c9c9c9"/></svg></span>
</div>

<h1 class="welcome">Welcome to the Kelvom Travel
  <svg class="welcome__notch" width="24" height="12"><path d="M0 0l12 12L24 0" fill="#fff" stroke="#dcdcdc"/><path d="M1 0h22" stroke="#fff" stroke-width="2"/></svg>
</h1>

<article class="service service--parties">
  <svg class="service__icon" width="48" height="44" viewBox="0 0 48 44">
    <rect x="2" y="22" width="20" height="6" rx="3" fill="#6f6f6f"/>
    <rect x="2" y="30" width="20" height="4" fill="#6f6f6f"/>
    <rect x="2" y="36" width="20" height="6" rx="2" fill="#6f6f6f"/>
    <path d="M26 14h18l-3 28H29z" fill="#6f6f6f"/>
    <path d="M37 14l6-14" stroke="#6f6f6f" stroke-width="2.5"/>
  </svg>
  <h2 class="service__title">Parties</h2>
  <p class="service__text">Kelvom Travel is a family run business. We pride ourselves on providing great service and value for money. We know</p>
</article>

<article class="service service--charters">
  <svg class="service__icon" width="50" height="46" viewBox="0 0 50 46">
    <rect x="2" y="2" width="46" height="22" rx="4" fill="#6f6f6f"/>
    <rect x="6" y="6" width="8" height="8" fill="#fff"/><rect x="17" y="6" width="8" height="8" fill="#fff"/><rect x="28" y="6" width="8" height="8" fill="#fff"/><rect x="39" y="6" width="6" height="8" fill="#fff"/>
    <circle cx="12" cy="25" r="4" fill="#6f6f6f"/><circle cx="38" cy="25" r="4" fill="#6f6f6f"/>
    <path d="M14 37h20" stroke="#6f6f6f" stroke-width="4"/><path d="M32 30l8 7-8 7z" fill="#6f6f6f"/>
  </svg>
  <h2 class="service__title">Charted Trips</h2>
  <p class="service__text">Kelvom Travel is a family run business. We pride ourselves on providing great service and value for money. We know</p>
</article>

<article class="service service--corporate">
  <svg class="service__icon" width="50" height="40" viewBox="0 0 50 40">
    <circle cx="11" cy="12" r="6" fill="#6f6f6f"/><circle cx="39" cy="12" r="6" fill="#6f6f6f"/><circle cx="25" cy="8" r="7" fill="#6f6f6f"/>
    <path d="M2 36v-10a9 9 0 0 1 18 0v10zM30 36v-10a9 9 0 0 1 18 0v10z" fill="#6f6f6f"/>
    <path d="M14 38v-14a11 11 0 0 1 22 0v14z" fill="#6f6f6f" stroke="#fff" stroke-width="2"/>
  </svg>
  <h2 class="service__title">Corporate Events</h2>
  <p class="service__text">Kelvom Travel is a family run business. We pride ourselves on providing great service and value for money. We know</p>
</article>

<footer class="site-footer">
  <p class="site-footer__copy">Copyright 2014 Kelvom Travel Pty Ltd. ACN: 412 557 083! - Powered by Loomwise</p>
  <div class="social social--footer">
    <span class="social__item"><svg width="28" height="28" viewBox="0 0 28 28"><circle cx="14" cy="14" r="12" fill="none" stroke="#c9c9c9" stroke-width="2.5"/><path d="M14 7v14M7 14h14" stroke="#c9c9c9" stroke-width="3"/></svg></span>
    <span class="social__item"><svg width="22" height="22"><circle cx="11" cy="11" r="9" fill="#c9c9c9"/></svg></span>
    <span class="social__item"><svg width="22" height="22"><circle cx="11" cy="11" r="9" fill="#c9c9c9"/></svg></span>
    <span class="social__item"><svg width="22" height="22"><circle cx="11" cy="11" r="9" fill="#c9c9c9"/></svg></span>
    <span class="social__item"><svg width="22" height="22"><circle cx="11" cy="11" r="9" fill="#c9c9c9"/></svg></span>
    <span class="social__item" style="border-right:1px solid var(--line)"><svg width="22" height="22"><circle cx="11" cy="11" r="9" fill="#c9c9c9"/></svg></span>
  </div>
</footer>

</body>
</html>
```